Solar for Wineries

I am looking for a 4 page "Renewable Products Brochure" I can used for initial customer contact. My customers are high-end winery owners and wine makers.

Our products are solar electric systems, solar thermal water heating systems and electric vehicle charging systems.

My customers have an high degree of connection to grapes, grape vines, flowing hills of vineyards and beautiful architecture. Green, purple and pastel colors play well.

A key aspect of our selling proposition is that we are a local company. We are their neighbor and their customer. We hire local workers, and bring a serious commitment to the success of our customers.

See our website: www.brantwickpower.com

Logos and pictures uploaded for Solar Winery Project

see posted file for new text content

For those who included the map in you designs, I posted a map with our logo at past installation sites.  Please use my new map, or add the logo at sites as indicated.   I would not add the logos on the map with the grape leaf background.

Thanks.

Brian

Target recipient: male or female, 50-65 years old, college educated, and business savvy. Interests:growing grapes and producing award winning wines.

It Company

• Lots of wine and grape pictures.
A map of the Tilbury Rd area of Plymouth California USA. would promote the idea of a local company.

Need pictures of our solar systems and electric vehicle chargers.
• No tech nuts and bolts pictures. No graphs or formulas.

```html
<!DOCTYPE html>
<html lang="en">
<head>
<meta charset="utf-8">
<title>Solar for Wineries – Brochure Spread</title>
<link rel="stylesheet" href="https://fonts.googleapis.com/css2?family=Archivo+Narrow:wght@400;500&display=swap">
<style>
  :root {
    --paper: #ffffff;
    --aqua: #b9f4ec;
    --cream: #f5f2b2;
    --ink: #2f3fcf;
    --vine-green: #6fa04a;
    --sky: #bfe0ee;
    --grape: #3b3fd6;
    --earth: #7a6a3a;
  }
  * { box-sizing: border-box; margin: 0; padding: 0; }
  html, body { width: 1200px; height: 776px; overflow: hidden; background: var(--paper); }
  .spread { position: relative; width: 1200px; height: 776px; overflow: hidden; background: var(--paper); }

  .band { position: absolute; }
  .band-aqua { background: var(--aqua); }
  .band-cream { background: var(--cream); }

  .photo { position: absolute; }

  .copy {
    position: absolute;
    font-family: "Archivo Narrow", "Arial Narrow", sans-serif;
    font-size: 8.3px;
    line-height: 10.4px;
    color: var(--ink);
    text-align: justify;
  }
  .copy p { margin-bottom: 10.4px; }
  .copy-left { left: 226px; top: 117px; width: 374px; }
  .copy-right { left: 652px; top: 117px; width: 333px; }
</style>
</head>
<body>
<main class="spread">

  <!-- colour fields -->
  <div class="band band-cream" style="left:303px; top:0; width:482px; height:98px;"></div>
  <div class="band band-cream" style="left:600px; top:98px; width:385px; height:448px;"></div>
  <div class="band band-cream" style="left:785px; top:98px; width:200px; height:0;"></div>
  <div class="band band-aqua" style="left:0; top:98px; width:402px; height:678px;"></div>
  <div class="band band-aqua" style="left:402px; top:98px; width:100px; height:192px;"></div>
  <div class="band band-aqua" style="left:212px; top:290px; width:388px; height:486px;"></div>
  <div class="band band-aqua" style="left:502px; top:290px; width:98px; height:0;"></div>

  <!-- left page imagery -->
  <div class="photo" role="img" aria-label="Ground-mounted solar panel array in a green vineyard"
       style="left:0; top:0; width:303px; height:97px; background:linear-gradient(180deg,#e8f2f6 0%,#b9cfa4 45%,#5d8a3a 100%);"></div>
  <div class="photo" role="img" aria-label="Rows of vines in autumn reds and golds under a blue sky"
       style="left:0; top:112px; width:212px; height:136px; background:linear-gradient(180deg,#cfe3f0 0%,#b86a5a 35%,#8a3f4a 60%,#6f9a3e 100%);"></div>
  <div class="photo" role="img" aria-label="Rooftop-style solar array in front of a white winery building"
       style="left:0; top:265px; width:212px; height:185px; background:linear-gradient(180deg,#c4e6ef 0%,#8fc6d6 30%,#3a6fb0 55%,#2a4f8f 100%);"></div>
  <div class="photo" role="img" aria-label="Illustrated cluster of purple grapes"
       style="left:10px; top:575px; width:82px; height:86px; background:radial-gradient(circle at 45% 55%,#5a5ef0 0%,#3438c8 60%,transparent 72%);"></div>
  <div class="photo" role="img" aria-label="Glasses of red and white wine"
       style="left:0; top:675px; width:105px; height:101px; background:linear-gradient(90deg,#d9b46a 0%,#8a2f2a 40%,#f0e2a8 70%,#b88a40 100%);"></div>
  <div class="photo" role="img" aria-label="Close-up of a bunch of dusty blue grapes"
       style="left:105px; top:675px; width:198px; height:101px; background:radial-gradient(circle at 50% 50%,#7d92c8 0%,#4a5a9a 55%,#2c3a6a 100%);"></div>

  <!-- right page imagery -->
  <div class="photo" role="img" aria-label="Sunlit green grape leaves"
       style="left:785px; top:0; width:415px; height:97px; background:linear-gradient(90deg,#4f8a2a 0%,#9fd05a 45%,#e4f4c8 70%,#6faa38 100%);"></div>
  <div class="photo" role="img" aria-label="Illustrated cluster of purple grapes"
       style="left:1105px; top:95px; width:90px; height:96px; background:radial-gradient(circle at 50% 55%,#5a5ef0 0%,#3438c8 60%,transparent 72%);"></div>
  <div class="photo" role="img" aria-label="Winery entrance sign beside a vineyard"
       style="left:985px; top:288px; width:215px; height:120px; background:linear-gradient(180deg,#cfe6f2 0%,#a9c88a 45%,#6a7a3a 100%);"></div>
  <div class="photo" role="img" aria-label="Stone winery sign with flower beds"
       style="left:985px; top:422px; width:215px; height:115px; background:linear-gradient(180deg,#5e8a3a 0%,#b8ad94 40%,#a8a096 65%,#d86aa8 100%);"></div>
  <div class="photo" role="img" aria-label="Solar thermal collectors on a wooden winery building among flowers"
       style="left:785px; top:550px; width:415px; height:226px; background:linear-gradient(160deg,#8fae5a 0%,#6a4a2e 35%,#3f7fd0 55%,#5a8a3a 80%,#c86aa8 100%);"></div>

  <!-- left page copy -->
  <section class="copy copy-left">
    <p>Wine producers of California are ideally positioned to provide leadership in renewable energy installation. Seldom is there an opportunity presented that has immediate financial benefit, increased operational efficiency and long term customer loyalty development as can now be achieved now by converting to eco-friendly energy producing sources.</p>
    <p>Central California is blessed with abundant amounts of sunlight, temperate climate, and lots of grape vines! All work together to provide wineries and grape growers with numerous opportunities to benefit from a variety of renewable energy resources.</p>
    <p>Your customers expect environmentally conscious practices will be used to produce their favorite wine. Minimal use of energy goes hand-in-hand with organic and natural farming techniques. Wineries that prominently display commitment to ecofriendly operations will benefit from customer goodwill.</p>
    <p>Whether it is production of solar electricity for improving energy efficiency of your customer-facing tasting rooms or for offsetting electrical costs for water pumping, installation of PV solar modules can effectively eliminate the majority of your electrical costs.</p>
    <p>Winery barrel-cleaning operations consume large amounts of propane? No problem; Solar hot water heating can be the answer. Recent progress in solar thermal panels has been remarkable. They produce hot water…. and lots of it! Modern winery operations can offset as much as 70% of water heating needs using solar thermal systems.</p>
    <p>Environmentally conscious wine club members will soon be arriving at tasting rooms around the wine country. They will have two things on their minds; where is the best wine tasting, and where can I recharge my EV? Forward-thinking business that offer electric charging stations will be sure to capture the business, if not the heart, of those visitors. EV charging costs can be predictably offset by on-site production of solar electricity.</p>
    <p>Solar electric systems used to “spin your meter backwards”, come in a variety of appearances. Field-deployed arrays, mounted on support structures, offer simple yet powerful, behind the scenes, producers of electricity. Solar arrays that are visible from customer occupied spaces can be constructed of truly beautiful all-glass panels. These aesthetically pleasing arrays can be effective shade structures for patio covers, or can be translucent for minimal light obstruction. Traditional roof-mounted installations are often preferred, providing shade to the building while minimizing the footprint compared to ground-mounted arrays.</p>
    <p>Solar thermal systems can be among the most cost effective of all renewable resources. Thermal collectors capture larger amounts of power from the sun than do PV electric collectors. That energy is used to heat (or preheat) your hot water, thereby drastically reducing propane or natural gas consumption. These systems come in a large range of sizes and efficiencies, ranging from the traditional simple flat panels, to modern collectors that track the sun from morning till evening, ensuring maximum consistent output. Modern tracking collectors range from two to 25 times more productive than older flat panel systems.</p>
  </section>

  <!-- right page copy -->
  <section class="copy copy-right">
    <p>Electric cars are here today. Correspondingly electric vehicle chargers are rapidly becoming an established requirement for commercial businesses. Literally hundreds of thousands of electric cars will enter California in the next few years. In the same way gasoline stations of the past morphed into purveyors of drinks and food, tomorrows “filling stations” will be restaurants, coffee shops….and wine tasting rooms.</p>
    <p>EV cars contain “telematics”, which dynamically show locations of approaching charging locations. These telematics become automatic advertisement opportunities for local business. Most EV chargers require between 30 and 120 minutes to transfer meaningful charge to the car; this establishes the minimum duration of your customer’s visits. EV charger installations can be installed as free gratis to your customers. Alternatively, chargers can be equipped with credit card swipe machines to enable revenue generation for your business.</p>
    <p>Numerous financial incentive programs are available to offset the cost of installing renewable equipment. While most state-funded programs have passed, the federal government still offers several incentives. Subject to renewal and restrictions, Federal programs include outright cash grants, incentive tax credits up to 30% of the system costs, and accelerated depreciation. Some of these benefits have recapture and rollover features. Any consideration of the ROI for renewable equipment should include consultation with your tax professional to ensure maximum benefits are achieved.</p>
    <p>Renewable energy systems can also reduce day-to-day costs of operations. California utilities provide commercial customers with solar electric systems the ability to opt-out of programs that impose cost penalties during high demand periods in the summer months. Resultant cost savings are significant.</p>
    <p>Brightvale Solar is located in the heart of the central California wine country. From our base in Cedar Flats California, we branch out to provide personal and local service to our customers and friends. Your neighbors from the local communities staff our work crews. You will not find a more responsive team, dedicated to providing long-term support to our customers. We are pleased to offer numerous reference customers in your area.</p>
    <p>Brightvale Solar is a division our parent company, Brantwick Electric. Many solar companies are just that, solar contractors. We hold contractors licensing for Solar (C46) and Electrical (C-10) and General Contracting (B lic). Brantwick Electric Corp was established in 1995, and Brightvale Solar began operations in 2006.</p>
  </section>

</main>
</body>
</html>
```